WeighTheMatterClearly.net, a blog on economics and social issues, needs a facelift.

Make my blog website more attractive and functional.
It needs a cover image. The purpose of the blog is to sort out errors the public discourse on current topics that affect timeless issues. It is to correct erroneous conclusions on public issues caused by ignoring relevant facts, misunderstandings of the facts upon which they base conclusions, and/or misanalysis of the facts. The topics vary widely.

I have in mind some kind of transition from an out of focus area to a focused area. At one time I used the attached image, but it gave no hint of a transition from a lack of clarity to clarity. I am wide open to other approaches to conveying that idea.

A particular improvement would be making the Subscribe button to be easier to find,

Target Market(s)

People interested in how timeless economic, social, constitutional, political philosophy, and governance ideals apply to current affairs.

Logo Text

While I would not rule it out, I don't have in mind that the logo will be different from the cover image. The essence of the blog is mostly captured by its name, Weigh the Matter Clearly.

Requirements
Must have
• Cover image. Webpages that are nice looking and appropriate to the seriousness of the blog.

FOLLOW and SHARE buttons in easily found places.
Nice to have
• Instructions as to how to transfer/set up what I receive from the designer to the WordPress website.

Suggestions on Fonts.

Suggested changes to the pages.

BTW: I had no help setting up the current page.
Should not have
• Anything that hints that I am interested in or facilitiates the receipt of money from followers.

```html
<!DOCTYPE html>
<html lang="en">
<head>
<meta charset="utf-8">
<title>Weigh the Matter Clearly</title>
<link href="https://fonts.googleapis.com/css2?family=Roboto:wght@400;500;700&family=Merriweather:wght@300;400;700&display=swap" rel="stylesheet">
<style>
:root{
  --brand:#8b1414;
  --ink:#222;
  --muted:#666;
  --rule:#e4e4e4;
  --navy:#0d1a33;
  --link:#2aa6e0;
  --white:#fff;
}
*{box-sizing:border-box;margin:0;padding:0}
html,body{width:1200px;height:2906px;overflow:hidden;background:var(--white)}
body{font-family:'Roboto',sans-serif;color:var(--ink);position:relative}
.abs{position:absolute}
.site-header{top:0;left:0;width:1200px;height:100px;border-top:3px solid var(--brand);background:var(--white)}
.site-title{left:45px;top:28px;font-size:35px;font-weight:700;letter-spacing:-.3px;color:#222}
.main-nav{top:42px;left:632px;display:flex;gap:36px;font-size:14px}
.main-nav a{color:#333;text-decoration:none}
.main-nav a.active{color:var(--brand)}
.btn{display:flex;align-items:center;justify-content:center;font-weight:700;font-size:14px;text-decoration:none}
.btn-solid{background:var(--brand);color:var(--white)}
.btn-outline{border:2px solid var(--brand);color:var(--brand);background:var(--white)}
.header-subscribe{left:946px;top:30px;width:142px;height:39px}
.hero{top:100px;left:0;width:1200px;height:523px;background:radial-gradient(ellipse at 60% 40%,#2d4a78 0%,#142648 45%,var(--navy) 100%)}
.hero-tagline{left:47px;top:21px;font-family:Arial,sans-serif;font-size:19px;font-weight:700;color:#e8ecf4}
.explore{left:0;width:1200px;top:372px;text-align:center;color:#fff;font-size:14px;letter-spacing:4px}
.explore svg{display:block;margin:6px auto 0}
.post{width:636px;height:365px;left:106px}
.post.featured{background:var(--white);box-shadow:0 2px 10px rgba(0,0,0,.12)}
.post-photo{position:absolute;left:0;top:0;width:250px;height:365px}
.post-rule{position:absolute;left:187px;top:34px;width:92px;height:2px;background:var(--brand)}
.post-title{position:absolute;left:292px;top:16px;width:312px;font-family:'Merriweather',serif;font-weight:300;font-size:23px;line-height:34px;color:#333}
.post-excerpt{position:absolute;left:292px;top:136px;width:285px;font-size:14px;line-height:26px;color:var(--muted)}
.post-more{position:absolute;left:466px;top:296px;width:140px;height:47px}
.profile{left:775px;top:572px;width:311px;height:365px;background:var(--white);box-shadow:0 2px 10px rgba(0,0,0,.12)}
.profile-band{position:absolute;left:0;top:0;width:311px;height:108px;background:var(--brand)}
.profile-avatar{position:absolute;left:93px;top:38px}
.profile-name{position:absolute;top:175px;width:100%;text-align:center;font-size:17px;font-weight:500}
.profile-role{position:absolute;top:203px;width:100%;text-align:center;font-size:17px;color:#888;font-weight:500}
.profile .about{position:absolute;left:87px;top:238px;width:140px;height:46px}
.profile .sub{position:absolute;left:87px;top:294px;width:140px;height:47px}
.sidebar{left:782px;width:306px}
.side-heading{font-family:'Merriweather',serif;font-weight:700;color:var(--brand);font-size:22px}
.top-list{list-style:none;margin-top:18px}
.top-list li{height:94px;border-bottom:1px solid var(--rule);padding-top:10px;padding-right:40px;font-size:14px;font-weight:500;line-height:26px;color:#555}
.top-list li:first-child{height:80px;padding-top:0}
.top-list li:last-child{border:none}
.sub-heading{font-family:'Merriweather',serif;font-weight:700;color:var(--brand);font-size:18px}
.sub-text{margin-top:16px;font-size:14px;line-height:24px;color:#666;width:280px}
.email{margin-top:12px;width:278px;height:48px;border:1px solid #bbb;display:flex;align-items:center;justify-content:center;font-size:14px;color:#888}
.sidebar .btn-solid.wide{margin-top:12px;width:278px;height:48px}
.res-heading{font-family:'Merriweather',serif;font-weight:700;color:var(--brand);font-size:18px;line-height:34px}
.res-item{margin-top:14px;font-size:14px;line-height:24px}
.res-item b{font-weight:500;color:#555}
.res-item a{display:block;color:var(--link);text-decoration:underline;font-size:14px}
.res-item .plain{color:#666}
.archive{left:529px;top:2710px;width:183px;height:47px}
.site-footer{left:0;top:2817px;width:1200px;height:89px;background:var(--brand);color:var(--white);font-size:14px}
.copy{position:absolute;left:110px;top:36px}
.foot-nav{position:absolute;left:615px;top:36px;display:flex;gap:36px}
.foot-nav a{color:var(--white);text-decoration:none}
.social{position:absolute;left:1007px;top:38px;display:flex;gap:18px}
.social span{width:12px;height:12px;border-radius:50%;background:var(--white);display:block}
</style>
</head>
<body>

<header class="abs site-header">
  <div class="abs site-title">WEIGH THE MATTER CLEARLY</div>
  <nav class="abs main-nav">
    <a class="active" href="#">HOME</a><a href="#">ABOUT</a><a href="#">CONTACT US</a>
  </nav>
  <a class="abs btn btn-solid header-subscribe" href="#">SUBSCRIBE</a>
</header>

<section class="abs hero" role="img" aria-label="Cover image: glowing network of connected points on a deep blue background, blurred at the edges and sharp in the centre">
  <p class="abs hero-tagline">A place to seek clarity on timeless issues and issues of the day.</p>
  <div class="abs explore">EXPLORE
    <svg width="22" height="18" viewBox="0 0 22 18"><path d="M3 2l8 7 8-7M3 9l8 7 8-7" fill="none" stroke="#fff" stroke-width="2.2"/></svg>
  </div>
</section>

<article class="abs post featured" style="top:572px">
  <div class="post-photo" role="img" aria-label="Photo of a smiling woman holding a clipboard" style="background:linear-gradient(160deg,#d9a9a6,#c98a86 60%,#a7645f)"></div>
  <span class="post-rule"></span>
  <h2 class="post-title">What’s Going On? – Part VII Black Lives Do Matter, Dashed Hopes</h2>
  <p class="post-excerpt">Parts I – VI[i] of this series described mostly well-intended policies that harmed Blacks and produced valid grievances. Let’s now sort out perhaps the single most debilitating and confounding consequence</p>
  <a class="btn btn-outline post-more" href="#">READ MORE</a>
</article>

<aside class="abs profile">
  <div class="profile-band"></div>
  <svg class="profile-avatar" width="125" height="125" viewBox="0 0 125 125" role="img" aria-label="Author avatar placeholder">
    <circle cx="62.5" cy="62.5" r="62" fill="#fff"/>
    <circle cx="62.5" cy="62.5" r="60" fill="#111"/>
    <ellipse cx="62.5" cy="55" rx="26" ry="32" fill="#fff"/>
    <path d="M30 125c4-22 18-34 32-34s28 12 32 34z" fill="#fff"/>
  </svg>
  <div class="profile-name">MARLON TREVE</div>
  <div class="profile-role">Blogger-Journalist</div>
  <a class="btn btn-outline about" href="#">ABOUT US</a>
  <a class="btn btn-solid sub" href="#">SUBSCRIBE</a>
</aside>

<article class="abs post" style="top:1004px">
  <div class="post-photo" role="img" aria-label="Photo of a woman shaking hands with a man across a desk" style="background:linear-gradient(170deg,#c9979c,#b47d83 55%,#6e4a52)"></div>
  <span class="post-rule"></span>
  <h2 class="post-title">What’s Going On? – Part VII Black Lives Do Matter, Dashed Hopes</h2>
  <p class="post-excerpt">Parts I – VI[i] of this series described mostly well-intended policies that harmed Blacks and produced valid grievances. Let’s now sort out perhaps the single most debilitating and confounding consequence</p>
  <a class="btn btn-outline post-more" href="#">READ MORE</a>
</article>

<article class="abs post" style="top:1435px">
  <div class="post-photo" role="img" aria-label="Photo of a person typing on a laptop seen from above" style="background:linear-gradient(170deg,#9d94a8,#b7adbc 50%,#c6a9a3)"></div>
  <span class="post-rule"></span>
  <h2 class="post-title">What’s Going On? – Part VII Black Lives Do Matter, Dashed Hopes</h2>
  <p class="post-excerpt">Parts I – VI[i] of this series described mostly well-intended policies that harmed Blacks and produced valid grievances. Let’s now sort out perhaps the single most debilitating and confounding consequence</p>
  <a class="btn btn-outline post-more" href="#">READ MORE</a>
</article>

<article class="abs post" style="top:1866px">
  <div class="post-photo" role="img" aria-label="Photo of a smiling woman with curly hair holding a tablet" style="background:linear-gradient(170deg,#7a4e4c,#b99596 50%,#d2c1c4)"></div>
  <span class="post-rule"></span>
  <h2 class="post-title">What’s Going On? – Part VII Black Lives Do Matter, Dashed Hopes</h2>
  <p class="post-excerpt">Parts I – VI[i] of this series described mostly well-intended policies that harmed Blacks and produced valid grievances. Let’s now sort out perhaps the single most debilitating and confounding consequence</p>
  <a class="btn btn-outline post-more" href="#">READ MORE</a>
</article>

<article class="abs post" style="top:2297px">
  <div class="post-photo" role="img" aria-label="Photo of many hands stacked together in teamwork" style="background:linear-gradient(160deg,#e9c3a4,#d9a38d 55%,#b97f70)"></div>
  <span class="post-rule"></span>
  <h2 class="post-title">What’s Going On? – Part VII Black Lives Do Matter, Dashed Hopes</h2>
  <p class="post-excerpt">Parts I – VI[i] of this series described mostly well-intended policies that harmed Blacks and produced valid grievances. Let’s now sort out perhaps the single most debilitating and confounding consequence</p>
  <a class="btn btn-outline post-more" href="#">READ MORE</a>
</article>

<aside class="abs sidebar" style="top:1022px">
  <h3 class="side-heading">Top post</h3>
  <ul class="top-list">
    <li>The Truth is still Hard For The Daily Ledger Times.</li>
    <li>What's Going On?-part VII Black Lives Do Matter Dashed Hopes</li>
    <li>The Quiet Algorithm-A Review</li>
    <li>What's Going On?-part VII Black Lives Do Matter The Stereotyping Problem</li>
    <li>What's Going On?-part VII Black Lives Do Matter Unfair Discriminatory Structures</li>
  </ul>
</aside>

<section class="abs sidebar" style="top:1630px">
  <h3 class="sub-heading">SUBSCRIBE TO BLOG</h3>
  <p class="sub-text">Enter your email address to subscribe to this blog and receive notifications of new posts by email.</p>
  <div class="email">Enter your email</div>
  <a class="btn btn-solid wide" href="#">SUBSCRIBE</a>
</section>

<section class="abs sidebar" style="top:1935px">
  <h3 class="res-heading">GREAT ONLINE RESOURCES<br>FOR INSIGHT</h3>
  <div class="res-item" style="margin-top:6px"><b>Harold Vance</b><a href="#">http://opinionhall.example/columnists/haroldvance/</a></div>
  <div class="res-item"><b>Nathan Corwell</b><a href="#">https://www.videoshare.example/user/NathanCorwell Videos</a></div>
  <div class="res-item"><span class="plain">The Institute for Civic Economics (ICE)</span><a href="#">https://ice-civic.org/</a></div>
  <div class="res-item"><b>Paul Ashby</b><a href="#">econdialogue.org</a></div>
  <div class="res-item"><b>CafeLiberal</b><a href="#">cafeliberal.com</a></div>
  <div class="res-item"><b>Oddnomics</b><a href="#">oddnomics.com</a></div>
</section>

<a class="abs btn btn-solid archive" href="#">VIEW FOR ARCHIVE</a>

<footer class="abs site-footer">
  <div class="copy">© Copyright 2020 Weigh the Matter Clearly | All Rights Reserved.</div>
  <nav class="foot-nav"><a href="#">Home</a><a href="#">About</a><a href="#">Contact us</a><a href="#">Privacy policy</a></nav>
  <div class="social" aria-label="Follow links"><span aria-label="Follow 1"></span><span aria-label="Follow 2"></span><span aria-label="Follow 3"></span></div>
</footer>

</body>
</html>
```